Tolvir Laundry and Dry Cleaning Poster

We need a Poster and Window Sticker for our Laundry and Dry cleaning shop (TOLVIR LAUNDRY AND DRY CLEANING).
info we like on the design. Logo is included
Company Name: Tolvir Laundry and Dry Cleaning
Slogan: It Comes Back Clean
Location: Kwelmo-Danfi, Accra
Working Hours: Mon-Sat 8am to 5pm
Tel: +233 30 418 7262
email:info@tolvirwash.example
website: www.tolvirwash.example
fb: fb.com/tolvirwash

Target Market(s)

Laundry Shop

Colors
33a6d7
9bcb3b

```html
<!DOCTYPE html>
<html lang="en">
<head>
<meta charset="UTF-8">
<title>Tolvir Laundry and Dry Cleaning Poster</title>
<link rel="stylesheet" href="https://fonts.googleapis.com/css2?family=Montserrat:wght@600;700&family=Oswald:wght@500&display=swap">
<style>
  :root {
    --brand-blue: #33a6d7;
    --sky-blue: #3fcdf2;
    --mint-green: #48e08c;
    --lime-top: #86f51a;
    --lime-bottom: #56b424;
    --foam-light: #e6f6fd;
    --foam-mid: #7fd0f4;
    --foam-deep: #1f8fdb;
    --white: #ffffff;
  }
  * { margin: 0; padding: 0; box-sizing: border-box; }
  html, body { width: 1200px; height: 1000px; overflow: hidden; background: var(--white); }
  .poster {
    position: relative;
    width: 1200px;
    height: 1000px;
    overflow: hidden;
    background: linear-gradient(to bottom, #ffffff 0%, #f7fcff 50%, #d6f0fc 72%, #bfe7fa 100%);
    font-family: "Montserrat", sans-serif;
  }
  .brand-mark {
    position: absolute;
    left: 95px;
    top: 25px;
    width: 310px;
    height: 310px;
    border-radius: 50%;
    background: var(--brand-blue);
  }
  .brand-name {
    position: absolute;
    left: 440px;
    top: 0;
    font-family: "Montserrat", sans-serif;
    font-weight: 700;
    font-size: 215px;
    line-height: 1;
    letter-spacing: -4px;
    color: var(--sky-blue);
  }
  .brand-subtitle {
    position: absolute;
    left: 448px;
    top: 262px;
    font-family: "Montserrat", sans-serif;
    font-weight: 600;
    font-size: 38px;
    letter-spacing: 0.5px;
    color: var(--mint-green);
  }
  .slogan-band {
    position: absolute;
    left: 0;
    top: 338px;
    width: 1200px;
    height: 150px;
    background: linear-gradient(to bottom, var(--lime-top), var(--lime-bottom));
    display: flex;
    align-items: center;
    justify-content: center;
  }
  .slogan {
    font-family: "Montserrat", sans-serif;
    font-weight: 600;
    font-size: 82px;
    letter-spacing: 3px;
    color: var(--white);
    text-shadow: 0 2px 4px rgba(0,0,0,0.25);
  }
  .foam {
    position: absolute;
    left: 0;
    bottom: 0;
    width: 1200px;
    height: 300px;
    background: radial-gradient(ellipse at 50% 0%, var(--foam-light) 0%, var(--foam-mid) 45%, var(--foam-deep) 100%);
    clip-path: path("M0 70 C 150 20, 300 110, 460 70 S 760 10, 900 80 S 1120 40, 1200 60 L 1200 300 L 0 300 Z");
  }
  .details {
    position: absolute;
    left: 0;
    top: 520px;
    width: 1200px;
    text-align: center;
  }
  .hours {
    font-family: "Montserrat", sans-serif;
    font-weight: 700;
    font-size: 84px;
    letter-spacing: 1px;
    line-height: 1.1;
    color: var(--sky-blue);
  }
  .location {
    margin-top: 6px;
    font-family: "Oswald", sans-serif;
    font-weight: 500;
    font-size: 64px;
    line-height: 1.1;
    color: var(--sky-blue);
    text-shadow: 0 0 6px #ffffff, 0 0 12px #ffffff;
  }
  .contact {
    position: absolute;
    left: 0;
    top: 740px;
    width: 1200px;
    text-align: center;
    font-family: "Oswald", sans-serif;
    font-weight: 500;
    font-size: 35px;
    line-height: 1.2;
    letter-spacing: 1px;
    color: var(--white);
    text-shadow: 0 2px 4px rgba(20,80,140,0.6);
  }
</style>
</head>
<body>
  <main class="poster">
    <div class="brand-mark"></div>
    <div class="brand-name">tolvir</div>
    <div class="brand-subtitle">LAUNDRY AND DRY CLEANING</div>

    <div class="slogan-band">
      <h1 class="slogan">IT COMES BACK CLEAN</h1>
    </div>

    <div class="foam" role="img" aria-label="Soap foam and bubbles along the bottom edge"></div>

    <section class="details">
      <p class="hours">Mon-Sat 8am to 5pm</p>
      <p class="location">Kwelmo-Danfi • Accra | +233-30-418-7262</p>
    </section>

    <section class="contact">
      <p>info@tolvirwash.example | tolvirwash.example</p>
      <p>fb.com/tolvirwash</p>
    </section>
  </main>
</body>
</html>
```